Velmora Resident Safety and Security

Need a website for our company. Please see attached outlines and files
Main Page
Velmora
Design – Install – Maintain
Supporting the Safety and Security needs of your Community
Best in Class Systems for the Safety and Security of your Residents and Staff
Your Trusted Advisor
Solutions
Systems tailored to the needs of your facility
Skilled Nursing Facilities
Long Term Care
CCRC’s
Assisted Living
Independent Living
Access Control
Maglocks
Keypads
Prox readers (key fob, card, etc.)
Wireless locks
Multi-Tennant
Perimeter doors
Resident Apartment doors
Nurse Call
Tone / Visual
Fixed Stations
Dome Lights
T/V+ Audio
Fixed Stations
Dome Lights
Audio communication
Wireless
Fixed Stations
Resident Pendants
Hybrid Systems
Wired and Wireless integrated for seamless notification and reporting.
CCTV
Surveillance systems to fit your security needs and your budget
Remote Access, Local or Cloud Storage
Good, Better, Best proposals
Wander management
Door Alarming
Detection of wandering resident
Remote alarming and alerts
Delay elopement to allow for redirection
Network Infrastructure
Modern infrastructure for modern systems
Conference and Telepresence
Professionally installed systems to allow for seamless clear communications between teams across infinite distances.
Our Team
Rolf Amundsen – President
Patricia Lowell – Vice President of Customer Success
Miles Forbush – Account Executive
Industry Associations
Harborline Collective
Massachusetts chapter of the National Guild of Elder Care Stewards
Contact Us
Phone (603) 555-0172
Email Info@Velmora.example
Facilities we serve
Independent Senior Living
Assisted Living
Memory Care
CCRC (Continuing Care Retirement Community)
Skilled Nursing / Rehab
Multi-Tenant
Outpatient Surgical Centers
Endoscopy Clinics
Acute Care
Urgent Care
Commercial Properties of all types
General notes
Imagery should invoke high tech, safety, security and include healthcare themes. the circuit board shield is our logo and a ghosted image as back ground or some animation that brings in the logo or the circuit board should be incorporated.
Velmora is a systems integration company specializing in low voltage solutions for healthcare facilities and senior living communities. The company aims to leverage its industry expertise, and innovative products to become the market leader in systems integration, focusing on enhancing safety and operational efficiency.
Vision and Mission: Velmora’s vision is to revolutionize integrated systems within healthcare and commercial environments by delivering innovative, reliable, and tailored solutions that enhance operational efficiency and patient care. The company is committed to setting new standards for resident safety and customer satisfaction.
Company Summary: Founded by experienced industry professionals, Velmora specializes in the design, installation, and maintenance of systems including Access Control, Nurse Call, Delayed Egress, network infrastructure, and overhead paging primarily for healthcare clients.
Products and Services: The company offers a comprehensive range of low voltage systems including Nurse Call (wired and wireless), Wander Management, Access Control, and wired/wireless network infrastructure tailored for senior living and healthcare facilities.
Mission Statement
Velmora was founded to fill a specific need. Senor living communities and healthcare facilities of all kinds face unique challenges in regards to technology and systems integration. Velmora is perfectly positioned with an experienced management team, skilled technicians, industry relationships with suppliers and facility management groups. We have built our reputation on excellent customer service and the highest standards of integrity. Velmora’s vision is to revolutionize integrated systems within healthcare and commercial environments by delivering innovative, reliable, and tailored solutions that enhance operational efficiency and patient care. We are committed to setting new standards for resident safety and customer satisfaction in every project we undertake.

Target Market(s)

Senior living communities staff and management

Industry/Entity Type

Systems Intergration

Coding

Coded - Design and coding required

Font styles to use
Serif
Sans Serif

Colors
0054AA
0677BA
7BADD7
CADEEF
E8F1F8
0094D4
00A9DD
6FCCEA
C7EBF8
E9F6FB

Requirements
Must have
• unique eye catching design including circuit board (PCB) type design and our supplied logo files

```html
<!DOCTYPE html>
<html lang="en">
<head>
<meta charset="utf-8">
<title>Velmora Resident Safety and Security</title>
<link rel="stylesheet" href="https://fonts.googleapis.com/css2?family=Noto+Serif:wght@700&family=Montserrat:wght@400;500;600&display=swap">
<style>
:root{
  --blue-deep:#0054AA;
  --blue-mid:#0677BA;
  --blue-bright:#0094D4;
  --blue-sky:#00A9DD;
  --blue-pale:#C7EBF8;
  --blue-ice:#E9F6FB;
  --navy-title:#1d3f8c;
  --ink:#111;
  --grey-text:#555;
  --white:#fff;
}
*{box-sizing:border-box;margin:0;padding:0}
html,body{width:1200px;height:4155px;overflow:hidden;background:var(--white)}
body{position:relative;font-family:"Montserrat",sans-serif;color:var(--ink)}
.abs{position:absolute}
.serif{font-family:"Noto Serif",serif;font-weight:700;letter-spacing:4px}
.accent{color:var(--navy-title)}

/* header */
.brand{left:120px;top:22px;display:flex;align-items:center;gap:10px;font-weight:600;font-size:26px;color:var(--blue-deep)}
.brand-dot{width:28px;height:28px;border-radius:50%;background:var(--blue-bright)}
.nav{top:24px;left:358px;display:flex;gap:38px;font-size:15px;font-weight:500;letter-spacing:1px}
.nav a{color:#333;text-decoration:none;position:relative}
.nav a.active{color:var(--blue-bright)}
.nav a.active::after{content:"";position:absolute;left:0;right:0;bottom:-14px;height:3px;background:var(--blue-bright)}
.btn{display:inline-flex;align-items:center;justify-content:center;background:linear-gradient(90deg,var(--blue-bright),#0b63d4);color:var(--white);font-weight:600;font-size:15px;letter-spacing:1.5px;border-radius:4px}
.btn-contact{left:948px;top:12px;width:139px;height:46px}

/* hero */
.hero-photo{left:0;top:83px;width:1200px;height:725px}
.hero-title{left:107px;top:210px;font-size:60px;line-height:80px;color:var(--navy-title)}
.hero-text{left:115px;top:381px;width:460px;font-size:16px;line-height:34px;letter-spacing:1px;color:#444}
.btn-start{left:114px;top:527px;width:138px;height:46px;color:#0b1c3d;font-size:15px}

/* sections */
.section-title{left:0;width:1200px;text-align:center;font-size:46px}
.products-sub{left:0;top:928px;width:1200px;text-align:center;font-size:16px;line-height:29px;letter-spacing:1px;color:var(--grey-text)}
.card{top:1016px;width:313px;height:289px;background:var(--white);box-shadow:0 2px 10px rgba(0,0,0,.15);border-radius:4px}
.card .ph{position:absolute;left:10px;top:12px;width:293px;height:224px;border-radius:3px}
.card p{position:absolute;left:0;right:0;top:254px;text-align:center;font-size:16px;letter-spacing:1.5px}
.arrow{top:1133px;width:24px;height:24px;border-radius:50%;display:flex;align-items:center;justify-content:center}

.solutions-photo{left:0;top:1398px;width:600px;height:440px;background:linear-gradient(120deg,#e9dcc4 0%,#cdb595 35%,#8d8f9e 70%,#3f4f7a 100%)}
.solutions-panel{left:600px;top:1398px;width:600px;height:440px;background:linear-gradient(135deg,#2aa6dc,#1f86c9)}
.solutions-panel h2{position:absolute;left:46px;top:38px;font-size:46px;color:var(--white)}
.solutions-panel .sub{position:absolute;left:46px;top:108px;font-size:16px;color:var(--white);letter-spacing:1px}
.solutions-list{position:absolute;left:46px;top:163px;list-style:none}
.solutions-list li{display:flex;align-items:center;gap:20px;height:44.5px;font-size:16px;font-weight:600;color:var(--white);letter-spacing:1.5px}
.solutions-list li::before{content:"";width:20px;height:20px;border-radius:50%;background:var(--blue-pale);opacity:.75}

.hub{left:440px;top:2005px;width:270px;height:270px;border-radius:50%;background:radial-gradient(circle at 40% 35%,#3cc0f4,#0a5fd0);box-shadow:0 0 0 10px var(--blue-ice);display:flex;align-items:center;justify-content:center;color:var(--white);font-weight:600;font-size:32px;letter-spacing:1px}
.fac-dot{width:58px;height:58px;border-radius:50%;background:linear-gradient(135deg,#1aa6e8,#0b5fcf);display:flex;align-items:center;justify-content:center;transform:translate(-29px,-29px);box-shadow:0 3px 8px rgba(11,95,207,.3)}
.fac-dot svg{width:28px;height:28px;fill:none;stroke:#fff;stroke-width:1.8;stroke-linecap:round;stroke-linejoin:round}
.fac-label{font-size:15.5px;letter-spacing:1px;color:#222;transform:translateY(-10px);white-space:nowrap}
.fac-label.r{transform:translate(-100%,-10px);text-align:right}

.mission{left:0;top:2516px;width:1200px;height:377px;background:linear-gradient(180deg,#1c52a8,#17479a)}
.mission h2{position:absolute;left:0;width:1200px;top:62px;text-align:center;font-size:46px;color:var(--white)}
.mission p{position:absolute;left:200px;width:800px;top:134px;text-align:center;font-size:15px;line-height:32px;letter-spacing:1px;color:var(--white)}
.btn-more{left:532px;top:2800px;width:138px;height:42px;font-size:15px}

.member{top:3052px;width:312px}
.member .ph{width:312px;height:224px}
.member h3{margin-top:26px;font-size:22px;font-weight:500;letter-spacing:2px}
.member span{display:block;margin-top:12px;font-size:14px;color:var(--blue-bright);letter-spacing:1px}

.assoc-title{left:111px;top:3446px;font-size:48px;line-height:52px}
.assoc{display:flex;align-items:center;gap:12px;font-size:22px;font-weight:600;color:#2c3f5c;line-height:28px}
.assoc-mark{width:44px;height:44px;border-radius:50%;background:#b9cfa3;flex:none}

/* footer */
.footer-shape{left:0;top:3630px;width:1200px;height:525px}
.foot-h{font-size:23px;color:var(--white);letter-spacing:2px}
.quick-links{left:116px;top:3850px;list-style:none}
.quick-links li{height:34.5px;font-size:14px;color:var(--white);letter-spacing:1px}
.foot-brand{left:450px;top:3800px;width:300px;display:flex;flex-direction:column;align-items:center;gap:14px;color:#1aa0ea;font-weight:600;font-size:42px}
.foot-brand .mark{width:150px;height:150px;border-radius:50%;background:linear-gradient(135deg,#1aa6e8,#0b4fc4)}
.socials{left:515px;top:4048px;display:flex;gap:9px}
.socials span{width:29px;height:29px;border-radius:50%;background:var(--white)}
.socials span:first-child{background:#1877d6}
.contact-row{left:858px;display:flex;align-items:center;gap:16px;font-size:14px;color:var(--white);letter-spacing:1px}
.contact-row svg{flex:none}
.foot-rule{left:116px;top:4110px;width:976px;height:1px;background:#777}
.copyright{left:0;width:1200px;top:4124px;text-align:center;font-size:13px;color:var(--white);letter-spacing:1px}
</style>
</head>
<body>

<!-- Header -->
<div class="abs brand"><span class="brand-dot"></span>Velmora</div>
<nav class="abs nav">
  <a class="active">Home</a><a>About Us</a><a>Services</a><a>Industries</a><a>Facilities</a>
</nav>
<a class="abs btn btn-contact">CONTACT US</a>

<!-- Hero -->
<svg class="abs hero-photo" viewBox="0 83 1200 725" width="1200" height="725" role="img" aria-label="Smiling senior woman on a sofa holding a resident call pendant">
  <defs>
    <linearGradient id="heroFill" x1="0" y1="0" x2="1" y2="0.3">
      <stop offset="0" stop-color="#eef3f8"/>
      <stop offset=".4" stop-color="#e2e6ea"/>
      <stop offset=".7" stop-color="#b9bcc2"/>
      <stop offset="1" stop-color="#ddd8d6"/>
    </linearGradient>
    <linearGradient id="band" x1="0" y1="0" x2="1" y2="0">
      <stop offset="0" stop-color="#0b63d4"/>
      <stop offset=".5" stop-color="#0a7ae0"/>
      <stop offset="1" stop-color="#1aa6e8"/>
    </linearGradient>
  </defs>
  <polygon points="0,83 1200,83 1200,686 600,790 0,656" fill="url(#heroFill)"/>
  <polygon points="0,656 600,775 1200,686 1200,692 600,808 0,664" fill="url(#band)"/>
</svg>
<h1 class="abs serif hero-title">DESIGN INSTALL<br>MAINTAIN</h1>
<p class="abs hero-text">Supporting the Safety and Security needs of your Community Best in Class Systems for the Safety and Security of your Residents and Staff Your Trusted Advisor</p>
<a class="abs btn btn-start">GET STARTED</a>

<!-- Products & Services -->
<h2 class="abs serif section-title" style="top:854px">Products <span class="accent">&amp; Services</span></h2>
<p class="abs products-sub">Velmora offers a comprehensive portfolio of low-voltage systems tailored<br>specifically for healthcare and senior living facilities, including:</p>

<div class="abs arrow" style="left:30px;background:var(--blue-bright)">
  <svg width="12" height="12" viewBox="0 0 12 12"><path d="M10 6H2M5 3 2 6l3 3" stroke="#fff" stroke-width="1.6" fill="none"/></svg>
</div>
<div class="abs arrow" style="left:1136px;background:#c9c9c9">
  <svg width="12" height="12" viewBox="0 0 12 12"><path d="M2 6h8M7 3l3 3-3 3" stroke="#fff" stroke-width="1.6" fill="none"/></svg>
</div>

<div class="abs card" style="left:110px">
  <div class="ph" role="img" aria-label="Hand holding a nurse call cord beside a wall call station" style="background:linear-gradient(120deg,#f1efeb,#dcd7cf 60%,#c6bfb5)"></div>
  <p>Nurse Call Systems</p>
</div>
<div class="abs card" style="left:440px">
  <div class="ph" role="img" aria-label="Senior woman using an access control keypad" style="background:linear-gradient(120deg,#2b2a2e,#5b4a3c 55%,#a08566)"></div>
  <p>Access Control Systems</p>
</div>
<div class="abs card" style="left:768px">
  <div class="ph" role="img" aria-label="Technician connecting fibre cables in a network switch" style="background:linear-gradient(160deg,#2d6fb8,#14335f 55%,#2f7f86)"></div>
  <p>Wired/Wireless Network</p>
</div>

<!-- Solutions -->
<div class="abs solutions-photo" role="img" aria-label="Senior couple sitting on a bed beside a wall call station"></div>
<section class="abs solutions-panel">
  <h2 class="serif">Our Solutions</h2>
  <p class="sub">Systems tailored to the needs of your facility</p>
  <ul class="solutions-list">
    <li>Skilled Nursing Facilities</li>
    <li>Long Term Care</li>
    <li>CCRC's</li>
    <li>Assisted Living</li>
    <li>Independent Living</li>
  </ul>
</section>

<!-- Facilities We Serve -->
<h2 class="abs serif section-title" style="top:1912px">Facilities <span class="accent">We Serve</span></h2>
<div class="abs hub">Velmora</div>

<div class="abs fac-dot" style="left:380px;top:2070px"><svg viewBox="0 0 28 28"><path d="M4 14 14 5l10 9M7 12v11h14V12M12 23v-6h4v6"/></svg></div>
<div class="abs fac-dot" style="left:388px;top:2143px"><svg viewBox="0 0 28 28"><circle cx="10" cy="7" r="2.5"/><circle cx="18" cy="7" r="2.5"/><path d="M7 23v-7l-1-4h8l-1 4v7M15 23v-7l-1-4h8l-1 4v7"/></svg></div>
<div class="abs fac-dot" style="left:412px;top:2224px"><svg viewBox="0 0 28 28"><path d="M14 23S5 17 5 11a4.5 4.5 0 0 1 9-1.5A4.5 4.5 0 0 1 23 11c0 6-9 12-9 12z"/></svg></div>
<div class="abs fac-dot" style="left:450px;top:2276px"><svg viewBox="0 0 28 28"><path d="M5 13a9 8 0 1 1 4 6.5L5 22l1.5-4A8 8 0 0 1 5 13z"/><circle cx="10" cy="13" r=".6"/><circle cx="14" cy="13" r=".6"/><circle cx="18" cy="13" r=".6"/></svg></div>
<div class="abs fac-dot" style="left:507px;top:2328px"><svg viewBox="0 0 28 28"><path d="M4 13 14 5l10 8M7 11v12h14V11"/><rect x="11" y="14" width="6" height="5"/></svg></div>
<div class="abs fac-dot" style="left:575px;top:2358px"><svg viewBox="0 0 28 28"><circle cx="14" cy="9" r="4"/><path d="M6 24c0-5 3.5-8 8-8s8 3 8 8zM12 20h4M14 18v4"/></svg></div>
<div class="abs fac-dot" style="left:644px;top:2322px"><svg viewBox="0 0 28 28"><path d="M8 20a6 6 0 0 1 12 0zM5 23h18M14 6v3M7 9l2 2M21 9l-2 2"/></svg></div>
<div class="abs fac-dot" style="left:700px;top:2275px"><svg viewBox="0 0 28 28"><path d="M14 4l8 3v6c0 6-4 9-8 11-4-2-8-5-8-11V7z"/><path d="M14 10v8M10 14h8"/></svg></div>
<div class="abs fac-dot" style="left:735px;top:2208px"><svg viewBox="0 0 28 28"><circle cx="14" cy="14" r="3"/><path d="M8 8a8.5 8.5 0 0 0 0 12M20 8a8.5 8.5 0 0 1 0 12M5 5a12.5 12.5 0 0 0 0 18M23 5a12.5 12.5 0 0 1 0 18"/></svg></div>
<div class="abs fac-dot" style="left:754px;top:2139px"><svg viewBox="0 0 28 28"><path d="M5 23V11h18v12zM3 23h22M10 11V6h8v5M14 14v6M11 17h6"/></svg></div>
<div class="abs fac-dot" style="left:760px;top:2066px"><svg viewBox="0 0 28 28"><path d="M7 24V5h10v19M17 10h5v14M4 24h21"/><path d="M10 9h1M13 9h1M10 13h1M13 13h1M10 17h1M13 17h1M19 14h1M19 18h1"/></svg></div>

<div class="abs fac-label r" style="left:330px;top:2068px">Independent Senior Living</div>
<div class="abs fac-label r" style="left:338px;top:2143px">Assisted Living</div>
<div class="abs fac-label r" style="left:374px;top:2224px">Memory Care</div>
<div class="abs fac-label r" style="left:407px;top:2285px">CCRC</div>
<div class="abs fac-label r" style="left:470px;top:2345px">Multi-Tenant</div>
<div class="abs fac-label" style="left:485px;top:2407px">Skilled Nursing / Rehab</div>
<div class="abs fac-label" style="left:690px;top:2328px">Urgent Care</div>
<div class="abs fac-label" style="left:745px;top:2277px">Acute Care</div>
<div class="abs fac-label" style="left:778px;top:2208px">Endoscopy Clinics</div>
<div class="abs fac-label" style="left:797px;top:2139px">Outpatient Surgical Centers</div>
<div class="abs fac-label" style="left:797px;top:2065px">Commercial Properties of all types</div>

<!-- Mission -->
<section class="abs mission">
  <h2 class="serif">Our Mision</h2>
  <p>Velmora was founded to fill a specific need. Senor living communities and healthcare facilities of all kinds face unique challenges in regards to technology and systems integration. Velmora is perfectly positioned with an experienced management team, skilled technicians, industry relationships with suppliers and facility management groups.</p>
</section>
<a class="abs btn btn-more">READ MORE</a>

<!-- Team -->
<h2 class="abs serif section-title" style="top:2963px">Our <span class="accent">Team</span></h2>
<div class="abs member" style="left:111px">
  <div class="ph" role="img" aria-label="Portrait of the company president in a navy suit" style="background:linear-gradient(120deg,#6b7d92,#3b4a60 55%,#1f2a3b)"></div>
  <h3>Rolf Amundsen</h3><span>President</span>
</div>
<div class="abs member" style="left:443px">
  <div class="ph" role="img" aria-label="Portrait of the vice president of customer success" style="background:linear-gradient(120deg,#5f6469,#8d8f92 50%,#cfcdca)"></div>
  <h3>Patricia Lowell</h3><span>Vice President of Customer Success</span>
</div>
<div class="abs member" style="left:775px">
  <div class="ph" role="img" aria-label="Portrait of the account executive in an office" style="background:linear-gradient(120deg,#b7bbc0,#7f8a99 50%,#2e3d5c)"></div>
  <h3>Miles Forbush</h3><span>Account Executive</span>
</div>

<!-- Associations -->
<h2 class="abs serif assoc-title">Industry<br><span style="color:#1a8fd8">Associations</span></h2>
<div class="abs assoc" style="left:485px;top:3476px"><span class="assoc-mark"></span>Harborline<br>Collective</div>
<div class="abs assoc" style="left:808px;top:3464px;font-size:18px;line-height:24px;width:290px"><span class="assoc-mark" style="background:#2c5c9c"></span>National Guild of Elder Care Stewards</div>

<!-- Footer -->
<svg class="abs footer-shape" viewBox="0 3630 1200 525" width="1200" height="525" aria-hidden="true">
  <defs>
    <linearGradient id="fband" x1="0" y1="0" x2="1" y2="0">
      <stop offset="0" stop-color="#1aa6e8"/><stop offset=".5" stop-color="#0b63d4"/><stop offset="1" stop-color="#1aa6e8"/>
    </linearGradient>
  </defs>
  <polygon points="0,3778 600,3638 1200,3778 1200,4155 0,4155" fill="url(#fband)"/>
  <polygon points="0,3790 600,3662 1200,3790 1200,4155 0,4155" fill="#121212"/>
</svg>

<h3 class="abs serif foot-h" style="left:113px;top:3796px">Quick Links</h3>
<ul class="abs quick-links">
  <li>Home</li><li>About Us</li><li>Services</li><li>Industries</li><li>Facilities</li><li>Contact Us</li>
</ul>

<div class="abs foot-brand"><span class="mark"></span>Velmora</div>
<div class="abs socials"><span></span><span></span><span></span><span></span></div>

<h3 class="abs serif foot-h" style="left:858px;top:3796px">Contact Info</h3>
<div class="abs contact-row" style="top:3851px">
  <svg width="22" height="22" viewBox="0 0 22 22"><circle cx="11" cy="11" r="11" fill="#fff"/><path d="M11 5a4 4 0 0 0-4 4c0 3 4 8 4 8s4-5 4-8a4 4 0 0 0-4-4z" fill="#121212"/><circle cx="11" cy="9" r="1.5" fill="#fff"/></svg>
  Lorem Ipsum,USA -437916
</div>
<div class="abs contact-row" style="top:3905px">
  <svg width="22" height="22" viewBox="0 0 22 22"><circle cx="11" cy="11" r="11" fill="#fff"/><path d="M7 6c1-1 2 0 2.5 1.5s-1 1.5-.5 2.5 1.5 2 2.5 2.5 1-1 2.5-.5S16 14 15 15c-2 2-9-5-8-9z" fill="#121212"/></svg>
  (603) 555-0172
</div>
<div class="abs contact-row" style="top:3959px">
  <svg width="22" height="22" viewBox="0 0 22 22"><circle cx="11" cy="11" r="11" fill="#fff"/><rect x="5.5" y="7" width="11" height="8" rx="1" fill="#121212"/><path d="M6 7.5l5 4 5-4" stroke="#fff" stroke-width="1" fill="none"/></svg>
  info@velmora.example
</div>

<div class="abs foot-rule"></div>
<p class="abs copyright">© 2025 Velmora .All Rights Reserved</p>

</body>
</html>
```